Hello, I would like a small logo change and template for business cards.
It will be much like the "Les Perles de Mona", with following changes:.
1. The round shape stays the same
2. The color will be the brown version I already have
3. The wording will be "MONA Arrange"

Hello, 

So the "brown" is actually Pantone 126

Good luck

```html
<!DOCTYPE html>
<html lang="en">
<head>
<meta charset="utf-8">
<title>Les Perles de Mona – Business Card</title>
<link href="https://fonts.googleapis.com/css2?family=Tenor+Sans&display=swap" rel="stylesheet">
<style>
  :root {
    --page-bg: #ffffff;
    --card-bg: #ffffff;
    --card-edge: #c8c8c8;
    --card-shadow: #555555;
    --band-brown: #2c2213;
    --pantone-gold: #a07a1a;
  }
  html, body {
    margin: 0;
    padding: 0;
    width: 1200px;
    height: 1000px;
    overflow: hidden;
    background: var(--page-bg);
  }
  .canvas {
    position: relative;
    width: 1200px;
    height: 1000px;
  }
  .card-shadow {
    position: absolute;
    left: 115px;
    top: 233px;
    width: 980px;
    height: 545px;
    background: var(--card-shadow);
  }
  .card {
    position: absolute;
    left: 107px;
    top: 225px;
    width: 978px;
    height: 543px;
    background: var(--card-bg);
    border: 1px solid var(--card-edge);
  }
  .brand-band {
    position: absolute;
    left: 0;
    top: 122px;
    width: 100%;
    height: 298px;
    background: var(--band-brown);
  }
  .brand-mark {
    position: absolute;
    left: 133px;
    top: 31px;
    width: 236px;
    height: 236px;
    border-radius: 50%;
    background: var(--pantone-gold);
    display: flex;
    align-items: center;
    justify-content: center;
  }
  .brand-name {
    margin: 0;
    font-family: "Tenor Sans", sans-serif;
    font-weight: 400;
    font-size: 25px;
    line-height: 1.3;
    text-align: center;
    color: var(--band-brown);
  }
  .tagline {
    position: absolute;
    left: 553px;
    top: 122px;
    margin: 0;
    font-family: "Tenor Sans", sans-serif;
    font-weight: 400;
    font-size: 40px;
    line-height: 52px;
    color: var(--pantone-gold);
    letter-spacing: 0.5px;
  }
</style>
</head>
<body>
  <div class="canvas">
    <div class="card-shadow"></div>
    <div class="card">
      <div class="brand-band">
        <div class="brand-mark">
          <p class="brand-name">Les Perles<br>de Mona</p>
        </div>
        <p class="tagline">MONA Arrange</p>
      </div>
    </div>
  </div>
</body>
</html>
```